The First Annual Fernwick Legacy Gala

Something similar to the attached but an attention grabber. It needs to attract people with money to spend!

```html
<!DOCTYPE html>
<html lang="en">
<head>
<meta charset="utf-8">
<title>Fernwick Legacy Gala</title>
<link href="https://fonts.googleapis.com/css2?family=Montserrat:wght@300;400;500;700;800&family=Roboto+Condensed:wght@300;400;700&family=Source+Sans+3:wght@400;600;700&display=swap" rel="stylesheet">
<style>
  :root {
    --page: #f3f3f4;
    --paper: #f4f2ee;
    --panel-top: #2c4f8f;
    --panel-bottom: #172f5e;
    --panel-glow: #3a62a8;
    --ink: #2b2f36;
    --navy: #1a3366;
    --gold: #d4a72c;
    --gold-light: #f2cf63;
    --rule: #b9a98a;
    --pill: #e6e2d8;
    --alert: #b8232a;
    --decor: #e8e2d3;
    --muted: #4a4f57;
  }
  * { margin: 0; padding: 0; box-sizing: border-box; }
  html, body { width: 1006px; height: 1200px; overflow: hidden; }
  body { background: var(--page); position: relative; }

  .flyer {
    position: absolute; left: 90px; top: 20px;
    width: 826px; height: 1160px;
    background: var(--paper); overflow: hidden;
    font-family: "Source Sans 3", sans-serif; color: var(--ink);
  }
  .decor-circle { position: absolute; border-radius: 50%; background: var(--decor); }
  .decor-circle.top-right { left: 589px; top: -48px; width: 236px; height: 236px; }
  .decor-circle.bottom-left { left: -8px; top: 997px; width: 220px; height: 220px; opacity: .8; }
  .accent-bar { position: absolute; left: 819px; top: 84px; width: 7px; height: 104px; background: var(--gold); }

  .title-panel {
    position: absolute; left: 29px; top: 0; width: 335px; height: 846px;
    background: linear-gradient(180deg, var(--panel-top) 0%, var(--panel-bottom) 100%);
    overflow: hidden;
    border-radius: 0 0 168px 168px / 0 0 190px 190px;
    color: #fff;
  }
  .title-panel .panel-glow {
    position: absolute; left: -50px; top: -40px; width: 200px; height: 200px;
    border-radius: 50%; background: var(--panel-glow);
  }
  .eyebrow {
    position: absolute; left: 35px; top: 66px;
    font-family: "Montserrat", sans-serif; font-weight: 700; font-size: 27px; line-height: 1.03;
    color: var(--gold-light);
  }
  .event-name {
    position: absolute; left: 33px; top: 140px;
    font-family: "Montserrat", sans-serif; font-weight: 800; font-size: 45px; line-height: 1.03;
    color: #ffffff; letter-spacing: -0.5px;
  }
  .event-name .thin {
    display: block; font-weight: 300; font-size: 48px; letter-spacing: 12px; margin-top: 2px;
    color: var(--gold-light);
  }
  .panel-rule { position: absolute; left: 35px; width: 243px; height: 2px; background: var(--gold); }
  .panel-rule.r1 { top: 317px; }
  .panel-rule.r2 { top: 414px; }
  .date {
    position: absolute; left: 35px; top: 334px;
    font-family: "Roboto Condensed", sans-serif; font-weight: 700; font-size: 27px; line-height: 1.25;
    letter-spacing: 2.4px; color: #ffffff;
  }
  .extra {
    position: absolute; left: 35px; top: 428px;
    font-family: "Roboto Condensed", sans-serif; font-size: 26px; line-height: 1.05; color: #ffffff;
  }
  .extra strong { font-weight: 700; font-size: 23px; display: block; color: var(--gold-light); }
  .extra span { font-weight: 300; }
  .venue-photo {
    position: absolute; left: 24px; top: 520px; width: 288px; height: 288px; border-radius: 50%;
    background: linear-gradient(180deg, #4e86c9 0%, #9dc0e6 38%, #f2f4f6 52%, #d7dde4 72%, #7d8a4e 86%, #5f6f36 100%);
    border: 4px solid var(--gold);
  }
  .social-badge {
    position: absolute; left: 246px; top: 532px; width: 66px; height: 66px; border-radius: 50%;
    background: var(--navy); border: 3px solid var(--gold);
    display: flex; align-items: center; justify-content: center;
    font-family: "Source Sans 3", sans-serif; font-weight: 700; font-size: 11px; color: #fff;
  }

  .headline {
    position: absolute; left: 382px; top: 88px; width: 400px;
    font-family: "Montserrat", sans-serif; font-weight: 800; font-size: 32px; line-height: 1.11;
    color: var(--navy);
  }
  .headline-rule { position: absolute; left: 382px; top: 211px; width: 106px; height: 4px; background: var(--gold); }
  .body-copy {
    position: absolute; left: 382px; width: 385px;
    font-size: 15.6px; line-height: 1.35; color: var(--ink);
  }
  .body-copy.p1 { top: 258px; }
  .body-copy.p2 { top: 354px; }
  .body-copy.p3 { top: 454px; }

  .follow-pill {
    position: absolute; left: 384px; top: 540px; width: 329px; height: 65px;
    background: var(--pill); border-radius: 16px;
    padding: 14px 14px; font-weight: 700; font-size: 12.5px; line-height: 1.3; color: var(--navy);
    display: flex; align-items: center;
  }
  .follow-icon {
    position: absolute; left: 723px; top: 546px; width: 51px; height: 55px; background: var(--pill);
    display: flex; align-items: center; justify-content: center;
  }
  .follow-icon i { width: 28px; height: 28px; border-radius: 50%; background: var(--gold); display: block; }

  .rule { position: absolute; left: 386px; width: 388px; height: 1px; background: var(--rule); }
  .rule.a { top: 649px; } .rule.b { top: 734px; } .rule.c { top: 840px; }
  .raffle, .donor {
    position: absolute; left: 386px; width: 400px;
    font-family: "Montserrat", sans-serif; font-size: 16.5px; line-height: 1.3; color: var(--muted);
  }
  .raffle { top: 669px; }
  .donor { top: 775px; }
  .raffle b, .donor b { color: var(--navy); font-weight: 800; }
  .donor-label {
    position: absolute; left: 386px; top: 754px; display: flex; align-items: center; gap: 3px;
    font-family: "Montserrat", sans-serif; font-weight: 700; font-size: 14.5px; color: var(--alert);
  }

  .tickets-heading {
    position: absolute; left: 46px; top: 876px;
    font-family: "Montserrat", sans-serif; font-weight: 700; font-size: 19px; color: var(--navy);
  }
  .tickets-rule { position: absolute; left: 116px; top: 910px; width: 148px; height: 2px; background: var(--gold); }
  .ticket { position: absolute; top: 951px; width: 120px; height: 80px; }
  .ticket.each { left: 49px; }
  .ticket.couple { left: 205px; }
  .ticket .price {
    position: absolute; left: 42px; right: 0; top: 8px; text-align: center;
    font-family: "Montserrat", sans-serif; font-weight: 800; font-size: 31px; line-height: 1;
  }
  .ticket .kind {
    position: absolute; left: 42px; right: 0; top: 45px; text-align: center;
    font-family: "Montserrat", sans-serif; font-weight: 700; font-size: 16px;
  }
  .ticket.each .price { color: var(--gold-light); }
  .ticket.each .kind { color: #fff; }
  .ticket.couple .price, .ticket.couple .kind { color: var(--navy); left: 34px; }

  .outlets-heading {
    position: absolute; left: 380px; top: 876px;
    font-family: "Montserrat", sans-serif; font-weight: 700; font-size: 19px; color: var(--navy);
  }
  .outlets { position: absolute; left: 380px; top: 907px; list-style: none; font-family: "Montserrat", sans-serif; }
  .outlets li { position: relative; padding-left: 12px; margin-bottom: 6px; font-size: 15.5px; line-height: 1.3; color: var(--muted); }
  .outlets li::before { content: ""; position: absolute; left: 0; top: 6px; width: 6px; height: 6px; background: var(--gold); }
  .outlets strong { display: block; color: #1b1e23; font-weight: 700; }

  .contact-pill {
    position: absolute; left: 48px; top: 1078px; width: 216px; height: 36px; border-radius: 18px;
    background: var(--navy); color: #fff; text-align: center;
    font-family: "Montserrat", sans-serif; font-weight: 700; font-size: 18.5px; line-height: 36px;
  }
  .contact-rule { position: absolute; height: 1px; background: var(--rule); }
  .contact-rule.top { left: 278px; top: 1088px; width: 548px; }
  .contact-rule.bottom { left: 50px; top: 1122px; width: 564px; }
  .contacts {
    position: absolute; left: 285px; top: 1093px;
    font-family: "Montserrat", sans-serif; font-size: 15px; color: var(--muted); white-space: nowrap;
  }
  .contacts b { color: var(--navy); font-weight: 700; }
  .contacts .gap { display: inline-block; width: 18px; }
  .footer-band {
    position: absolute; left: 246px; top: 1134px; width: 600px; height: 30px;
    background: linear-gradient(90deg, var(--panel-top), var(--panel-bottom));
    border-top: 3px solid var(--gold);
    border-radius: 36px 0 0 0;
  }
</style>
</head>
<body>
<main class="flyer">
  <div class="decor-circle top-right"></div>
  <div class="decor-circle bottom-left"></div>
  <div class="accent-bar"></div>

  <section class="title-panel">
    <div class="panel-glow"></div>
    <p class="eyebrow">THE FIRST<br>ANNUAL</p>
    <h1 class="event-name">FERNWICK<br>LEGACY<span class="thin">GALA</span></h1>
    <div class="panel-rule r1"></div>
    <p class="date">APRIL 23, 2022<br>STARTING AT 5:00 PM</p>
    <div class="panel-rule r2"></div>
    <p class="extra"><strong>WITH</strong><span>COCKTAIL HOUR</span></p>
    <div class="venue-photo" role="img" aria-label="Photo of the white community center building under a blue sky with green lawn"></div>
    <div class="social-badge">Townboard</div>
  </section>

  <h2 class="headline">LIVE AUCTION, SILENT AUCTION, RAFFLE AND A CASH BAR!</h2>
  <div class="headline-rule"></div>

  <p class="body-copy p1">Come on out to the Fernwick Community Center for a delicious prime rib dinner, drinks, entertainment and more! There will be plenty of amazing auction items for everyone to choose from.</p>
  <p class="body-copy p2">All proceeds will go to the Fernwick Community Center. We will share some history of the school and each year we will highlight a local family. This year will be the Hartwell family who have been here for generations!</p>
  <p class="body-copy p3">High Side Barn, dirt bike, custom knives, a pack trip and so much more!</p>

  <div class="follow-pill">Follow the Fernwick Community Center's Townboard page to see all the auction items available!</div>
  <div class="follow-icon"><i></i></div>

  <div class="rule a"></div>
  <p class="raffle">TICKETS FOR THE 10X12 HIGH SIDE BARN<br><b>$25</b> EACH OR 5 FOR <b>$100</b></p>
  <div class="rule b"></div>
  <div class="donor-label">
    <svg width="17" height="17" viewBox="0 0 17 17" aria-hidden="true"><rect x="1" y="2" width="14" height="14" fill="none" stroke="#b8232a" stroke-width="2"/><path d="M4 8.5l3 3 8-9" fill="none" stroke="#b8232a" stroke-width="2.4"/></svg>
    DONATED BY:
  </div>
  <p class="donor">SUMMIT SHED WORKS OF LARKSTON<br>VALUE <b>$6500</b></p>
  <div class="rule c"></div>

  <h3 class="tickets-heading">TICKETS FOR THE EVENT ARE:</h3>
  <div class="tickets-rule"></div>
  <div class="ticket each">
    <svg width="120" height="80" viewBox="0 0 120 80" aria-hidden="true">
      <rect x="2" y="3" width="116" height="74" fill="#1a3366" stroke="#d4a72c" stroke-width="3" stroke-dasharray="3 2"/>
      <line x1="32" y1="8" x2="32" y2="72" stroke="#d4a72c" stroke-width="1.5" stroke-dasharray="3 3"/>
    </svg>
    <span class="price">$50</span><span class="kind">EACH</span>
  </div>
  <div class="ticket couple">
    <svg width="120" height="80" viewBox="0 0 120 80" aria-hidden="true">
      <rect x="2" y="3" width="116" height="74" fill="#d4a72c" stroke="#1a3366" stroke-width="3" stroke-dasharray="3 2"/>
      <line x1="24" y1="8" x2="24" y2="72" stroke="#1a3366" stroke-width="1.5" stroke-dasharray="3 3"/>
    </svg>
    <span class="price">$90</span><span class="kind">COUPLE</span>
  </div>

  <h3 class="outlets-heading">Get your tickets from</h3>
  <ul class="outlets">
    <li><strong>Summit Shed Works in Larkston</strong>42 Alder Rd, Larkston</li>
    <li><strong>Ridgecrest Realty</strong>118 E Birch St. Larkston</li>
    <li><strong>Fernwick Store</strong>6120 County Route 44, Fernwick</li>
  </ul>

  <div class="contact-rule top"></div>
  <div class="contact-pill">Or get them from</div>
  <p class="contacts"><b>Dana Morrow</b> (555) 214 - 0187<span class="gap"></span><b>Jodie Fenn</b> (555) 362 - 0419</p>
  <div class="contact-rule bottom"></div>
  <div class="footer-band"></div>
</main>
</body>
</html>
```